Partlow Law Stationery - Letterhead, Envelopes, Business Cards

We need high quality business stationery for our Personal Injury Law Firm located in Houston, Texas. The design should include the logo, Partlow Law Group, PLLC, 713-555-0148, 2750 Marlowe Crescent, Suite 318, Houston, Texas 77099 www.PartlowLaw.example. The colors are blue and white. The letterhead should also include the Attorneys - Marcy Teague, Everett K. Partlow and Dorian Fisk.

```html
<!DOCTYPE html>
<html lang="en">
<head>
<meta charset="utf-8">
<title>Partlow Law Stationery</title>
<link href="https://fonts.googleapis.com/css2?family=Montserrat:wght@400;500;600;700&display=swap" rel="stylesheet">
<style>
  :root {
    --navy: #33375a;
    --navy-soft: #41466b;
    --paper: #fbfbf9;
    --ink: #2a2c3e;
    --body: #6b6d78;
    --backdrop: #e9e7e3;
    --rule: #33375a;
  }
  * { box-sizing: border-box; margin: 0; padding: 0; }
  html, body { width: 1200px; height: 1200px; overflow: hidden; }
  body {
    background: var(--backdrop);
    font-family: "Montserrat", sans-serif;
    color: var(--ink);
    position: relative;
  }
  .sheet {
    position: absolute;
    background: var(--paper);
    box-shadow: 0 6px 18px rgba(40, 40, 50, 0.12);
    overflow: hidden;
  }
  .brand-square {
    position: absolute;
    background: linear-gradient(160deg, var(--navy-soft), var(--navy));
    display: flex;
    align-items: center;
    justify-content: center;
  }
  .brand-name {
    color: #ffffff;
    font-weight: 600;
    letter-spacing: 0.06em;
    text-transform: uppercase;
    text-align: center;
    line-height: 1.25;
  }
  .icon {
    display: inline-flex;
    align-items: center;
    justify-content: center;
    background: var(--navy);
    border-radius: 3px;
    flex: none;
  }
  .icon svg { fill: #ffffff; }

  /* Letterhead */
  .letterhead { left: 40px; top: 236px; width: 560px; height: 724px; }
  .letterhead .brand-square { left: 300px; top: 0; width: 140px; height: 118px; }
  .letterhead .brand-name { font-size: 15px; }
  .letter-masthead {
    position: absolute; left: 52px; top: 30px; width: 230px;
    color: var(--navy);
  }
  .firm-name { font-size: 11.5px; font-weight: 600; letter-spacing: 0.04em; }
  .masthead-label { font-size: 9px; font-weight: 700; margin-top: 10px; letter-spacing: 0.04em; }
  .masthead-names { font-size: 9px; line-height: 1.5; margin-top: 2px; color: var(--ink); letter-spacing: 0.02em; }
  .letter-heading {
    position: absolute; left: 52px; top: 150px; width: 470px;
    font-size: 14.5px; font-weight: 500; line-height: 1.45; letter-spacing: 0.04em;
  }
  .letter-body {
    position: absolute; left: 52px; top: 208px; width: 460px;
    font-size: 9.2px; line-height: 1.75; color: var(--body); letter-spacing: 0.02em;
  }
  .letter-body p { margin-bottom: 11px; }
  .signature {
    position: absolute; left: 250px; top: 560px; width: 180px; height: 46px;
    background: #ecebe8; border-radius: 4px;
  }
  .letter-footer {
    position: absolute; left: 0; right: 0; top: 662px; height: 40px;
    background: var(--navy);
    clip-path: polygon(0 0, 86% 0, 100% 100%, 0 100%);
    display: flex; align-items: center; gap: 16px;
    padding-left: 28px;
    color: #ffffff; font-size: 9px; letter-spacing: 0.05em;
  }
  .letter-footer .item { display: flex; align-items: center; gap: 7px; }
  .letter-footer .icon { background: #ffffff; width: 14px; height: 14px; }
  .letter-footer .icon svg { fill: var(--navy); }
  .letter-footer .address { line-height: 1.35; }

  /* Envelope */
  .envelope { left: 640px; top: 80px; width: 520px; height: 270px; }
  .envelope .brand-square { left: 32px; top: 16px; width: 130px; height: 122px; }
  .envelope .brand-name { font-size: 14px; }
  .envelope-contact { position: absolute; left: 278px; top: 128px; }
  .attorneys-title { font-weight: 700; font-size: 14px; letter-spacing: 0.02em; }
  .attorneys-names { font-size: 9.5px; margin-top: 3px; letter-spacing: 0.02em; }
  .contact-list { list-style: none; margin-top: 8px; }
  .contact-list li { display: flex; align-items: flex-start; gap: 8px; font-size: 10px; line-height: 1.35; margin-bottom: 5px; letter-spacing: 0.04em; }
  .contact-list .icon { width: 13px; height: 13px; margin-top: 1px; }

  /* Business card front */
  .card-front { left: 700px; top: 410px; width: 400px; height: 229px; }
  .card-front .brand-square { left: 282px; top: 54px; width: 100px; height: 100px; }
  .card-front .brand-name { font-size: 10.5px; }
  .card-front-text { position: absolute; left: 34px; top: 40px; width: 230px; }
  .card-front-text .attorneys-names { font-size: 9.5px; line-height: 1.4; }
  .card-rule { border: 0; border-top: 1px solid var(--rule); margin: 10px 0 8px; width: 210px; }
  .card-front-text .contact-list { margin-top: 0; }
  .card-front-text .contact-list li { font-size: 9.5px; margin-bottom: 4px; }

  /* Business card back */
  .card-back { left: 700px; top: 672px; width: 400px; height: 229px; }
  .card-back .band { position: absolute; top: 0; bottom: 0; width: 82px; background: var(--navy); }
  .card-back .band-left { left: 0; }
  .card-back .band-right { right: 0; }
  .card-back .center-mark {
    position: absolute; left: 82px; right: 82px; top: 0; bottom: 0;
    display: flex; align-items: center; justify-content: center;
    color: var(--navy); font-weight: 600; font-size: 17px;
    letter-spacing: 0.06em; text-transform: uppercase; text-align: center; line-height: 1.25;
  }
</style>
</head>
<body>
<svg width="0" height="0" style="position:absolute" aria-hidden="true">
  <defs>
    <symbol id="i-phone" viewBox="0 0 24 24"><path d="M6.6 10.8a15 15 0 0 0 6.6 6.6l2.2-2.2c.3-.3.7-.4 1-.2 1.1.4 2.3.6 3.6.6.6 0 1 .4 1 1V20c0 .6-.4 1-1 1A17 17 0 0 1 3 4c0-.6.4-1 1-1h3.5c.6 0 1 .4 1 1 0 1.3.2 2.5.6 3.6.1.3 0 .7-.2 1z"/></symbol>
    <symbol id="i-globe" viewBox="0 0 24 24"><path d="M12 2a10 10 0 1 0 0 20 10 10 0 0 0 0-20zm6.9 6h-2.9a15.6 15.6 0 0 0-1.4-3.6A8 8 0 0 1 18.9 8zM12 4c.8 1.2 1.5 2.5 1.9 4h-3.8c.4-1.5 1.1-2.8 1.9-4zM4.3 14a8 8 0 0 1 0-4h3.4a16 16 0 0 0 0 4zm.8 2h2.9c.3 1.300.8 2.5 1.4 3.6A8 8 0 0 1 5.1 16zM8 8H5.1a8 8 0 0 1 4.3-3.6C8.8 5.5 8.3 6.7 8 8zm4 12c-.8-1.2-1.5-2.5-1.9-4h3.8c-.4 1.5-1.1 2.8-1.9 4zm2.3-6H9.7a14.7 14.7 0 0 1 0-4h4.6a14.7 14.7 0 0 1 0 4zm.3 5.6c.6-1.1 1.1-2.3 1.4-3.6h2.9a8 8 0 0 1-4.3 3.6zM16.3 14a16 16 0 0 0 0-4h3.4a8 8 0 0 1 0 4z"/></symbol>
    <symbol id="i-pin" viewBox="0 0 24 24"><path d="M12 2a7 7 0 0 0-7 7c0 5.2 7 13 7 13s7-7.8 7-13a7 7 0 0 0-7-7zm0 9.5a2.5 2.5 0 1 1 0-5 2.5 2.5 0 0 1 0 5z"/></symbol>
  </defs>
</svg>

<!-- Letterhead -->
<section class="sheet letterhead">
  <div class="letter-masthead">
    <div class="firm-name">Partlow Law Group, PLLC</div>
    <div class="masthead-label">Attorneys</div>
    <div class="masthead-names">Marcy Teague<br>Everett K. Partlow<br>Dorian Fisk</div>
  </div>
  <div class="brand-square"><span class="brand-name">Partlow<br>Law</span></div>
  <h1 class="letter-heading">Lorem ipsum dolor sit amet, consectetur adipiscing elit. Morbi non dapibus tellus. Duis ut rhoncus risus.</h1>
  <div class="letter-body">
    <p>Lorem ipsum dolor sit amet, consectetur adipiscing elit. Ut mauris turpis, porttitor quis dictum nec, interdum sit amet risus. Proin id porttitor diam. Integer ornare purus sit amet dui tristique fermentum. Sed iaculis laoreet urna vel molestie. Morbi quam augue, consectetur eu venenatis sed, euismod in velit.</p>
    <p>Cras ultricies velit sed nibh pretium vehicula. Morbi ultrices, libero sit amet condimentum lobortis, tortor metus elementum leo, a varius sapien dui eget tellus. Integer quis ligula dui. In viverra orci ornare massa ultrices, quis hendrerit ipsum ultricies. Nulla lacinia semper nulla blandit ultricies. Nullam pretium luctus sagittis. Ut ac odio elit, sed feugiat sem.</p>
    <p>Proin dui enim, tempus sit amet lacinia non, gravida quis ante. Morbi et est lectus, quis placerat turpis. Duis mattis, massa a venenatis euismod, libero enim dictum elit, ac aliquam massa tellus vitae mi. Morbi in elit id ante elementum tincidunt eget ac erat. Ut vitae ipsum sed dolor convallis accumsan. Morbi viverra elit sed ligula consectetur ornare. Donec id lorem dui, non tempus odio.</p>
  </div>
  <div class="signature" role="img" aria-label="Handwritten signature of Marcy Teague"></div>
  <footer class="letter-footer">
    <span class="item"><span class="icon"><svg width="9" height="9"><use href="#i-phone"/></svg></span>713-555-0148</span>
    <span class="item"><span class="icon"><svg width="9" height="9"><use href="#i-globe"/></svg></span>www.PartlowLaw.example</span>
    <span class="item"><span class="icon"><svg width="9" height="9"><use href="#i-pin"/></svg></span><span class="address">2750 Marlowe Crescent,<br>Suite 318, Houston, Texas 77099</span></span>
  </footer>
</section>

<!-- Envelope -->
<section class="sheet envelope">
  <div class="brand-square"><span class="brand-name">Partlow<br>Law</span></div>
  <div class="envelope-contact">
    <div class="attorneys-title">Attorneys</div>
    <div class="attorneys-names">Marcy Teague | Everett K. Partlow | Dorian Fisk</div>
    <ul class="contact-list">
      <li><span class="icon"><svg width="8" height="8"><use href="#i-phone"/></svg></span>713-555-0148</li>
      <li><span class="icon"><svg width="8" height="8"><use href="#i-globe"/></svg></span>www.PartlowLaw.example</li>
      <li><span class="icon"><svg width="8" height="8"><use href="#i-pin"/></svg></span><span>2750 Marlowe Crescent,<br>Suite 318, Houston, Texas 77099</span></li>
    </ul>
  </div>
</section>

<!-- Business card, front -->
<section class="sheet card-front">
  <div class="card-front-text">
    <div class="attorneys-title">Attorneys</div>
    <div class="attorneys-names">Marcy Teague<br>Everett K. Partlow<br>Dorian Fisk</div>
    <hr class="card-rule">
    <ul class="contact-list">
      <li><span class="icon"><svg width="8" height="8"><use href="#i-phone"/></svg></span>713-555-0148</li>
      <li><span class="icon"><svg width="8" height="8"><use href="#i-globe"/></svg></span>www.PartlowLaw.example</li>
      <li><span class="icon"><svg width="8" height="8"><use href="#i-pin"/></svg></span><span>2750 Marlowe Crescent,<br>Suite 318, Houston, Texas 77099</span></li>
    </ul>
  </div>
  <div class="brand-square"><span class="brand-name">Partlow<br>Law</span></div>
</section>

<!-- Business card, back -->
<section class="sheet card-back">
  <div class="band band-left"></div>
  <div class="center-mark">Partlow<br>Law</div>
  <div class="band band-right"></div>
</section>
</body>
</html>
```